Fitness Tracker for Fitness Club

We need a graphic design for a fitness app.

The app will display videos of live workouts, provide the ability to communicate to a trainer through an inbox, and the ability to track weight over time.

The layout provided is the current demo mobile html application, we would like to change this to a custom app and would like a new design, something that is clean and current. Something like stridely feel. User should feel like the app is clean and cutting edge.

The current demo is to display functionality only, we are hoping for a complete redesign of the app.

```html
<!DOCTYPE html>
<html lang="en">
<head>
<meta charset="utf-8">
<title>Kestrel Fitness – Home Screen</title>
<link rel="stylesheet" href="https://fonts.googleapis.com/css2?family=Roboto+Condensed:wght@400;700&family=Roboto:wght@400;500&display=swap">
<style>
  :root {
    --bg: #ece6f8;
    --brand-blue: #1b5cc4;
    --brand-blue-dark: #134aa6;
    --text-blue: #1a55c0;
    --caption-band: #2a2e36;
    --row-bg: #ffffff;
    --row-line: #d9d9d9;
    --footer-grey: #efefef;
    --chevron: #b9b9b9;
    --photo-top: #dfe7ee;
    --photo-mid: #9fc3d9;
    --photo-low: #3a4048;
  }
  * { box-sizing: border-box; margin: 0; padding: 0; }
  html, body { width: 1200px; height: 1000px; overflow: hidden; }
  body {
    background: var(--bg);
    font-family: "Roboto", Arial, sans-serif;
    display: flex;
    align-items: center;
    justify-content: center;
  }
  .app-screen {
    width: 540px;
    height: 960px;
    background: var(--row-bg);
    display: flex;
    flex-direction: column;
    overflow: hidden;
    box-shadow: 0 20px 50px rgba(60, 40, 110, 0.18);
  }
  .status-bar {
    height: 36px;
    background: var(--brand-blue);
    color: #fff;
    font-size: 15px;
    display: grid;
    grid-template-columns: 1fr auto 1fr;
    align-items: center;
    padding: 0 14px;
  }
  .status-bar .signal { display: flex; align-items: center; gap: 6px; }
  .status-bar .battery { justify-self: end; display: flex; align-items: center; gap: 6px; }
  .app-header {
    height: 80px;
    background: var(--brand-blue);
    color: #fff;
    display: flex;
    align-items: center;
    justify-content: center;
    font-family: "Roboto Condensed", "Arial Narrow", sans-serif;
    font-weight: 700;
    font-size: 30px;
    letter-spacing: 0.5px;
  }
  .video-of-day { position: relative; height: 456px; }
  .video-photo {
    height: 400px;
    background:
      radial-gradient(ellipse at 30% 40%, var(--photo-mid) 0%, transparent 45%),
      linear-gradient(180deg, var(--photo-top) 0%, #c9d4dc 55%, var(--photo-low) 100%);
  }
  .play-button {
    position: absolute;
    left: 50%;
    top: 200px;
    transform: translate(-50%, -50%);
  }
  .video-caption {
    height: 56px;
    background: var(--caption-band);
    color: #fff;
    font-family: "Roboto Condensed", "Arial Narrow", sans-serif;
    font-size: 22px;
    display: flex;
    align-items: center;
    justify-content: center;
  }
  .menu-list { list-style: none; }
  .menu-item {
    height: 90px;
    border-bottom: 1px solid var(--row-line);
    display: flex;
    align-items: center;
    padding: 0 26px 0 28px;
    gap: 22px;
  }
  .menu-item .icon { width: 40px; height: 40px; flex: none; }
  .menu-item .label {
    flex: 1;
    color: var(--text-blue);
    font-family: "Roboto Condensed", "Arial Narrow", sans-serif;
    font-size: 24px;
    text-transform: uppercase;
  }
  .menu-item .chevron { width: 20px; height: 12px; }
  .list-footer { flex: 1; background: var(--footer-grey); }
</style>
</head>
<body>
  <main class="app-screen">
    <div class="status-bar">
      <span class="signal">●●●○○ Carrier
        <svg width="16" height="12" viewBox="0 0 16 12"><path d="M1 4a10 10 0 0 1 14 0M3.5 6.5a6.5 6.5 0 0 1 9 0M6 9a3 3 0 0 1 4 0" fill="none" stroke="#fff" stroke-width="1.6"/></svg>
      </span>
      <span class="time">7:28 PM</span>
      <span class="battery">100%
        <svg width="28" height="12" viewBox="0 0 28 12"><rect x="0.5" y="0.5" width="24" height="11" rx="2" fill="none" stroke="#fff"/><rect x="2" y="2" width="21" height="8" fill="#fff"/><rect x="25.5" y="4" width="2" height="4" fill="#fff"/></svg>
      </span>
    </div>

    <header class="app-header">KESTREL FITNESS</header>

    <section class="video-of-day">
      <div class="video-photo" role="img" aria-label="Photo of two people training on elliptical machines in a bright gym"></div>
      <svg class="play-button" width="100" height="100" viewBox="0 0 100 100" aria-label="Play video">
        <circle cx="50" cy="50" r="48" fill="rgba(255,255,255,0.35)" stroke="rgba(255,255,255,0.7)" stroke-width="2"/>
        <path d="M40 30 L70 50 L40 70 Z" fill="rgba(255,255,255,0.85)"/>
      </svg>
      <div class="video-caption">On Demand Video of the Day</div>
    </section>

    <ul class="menu-list">
      <li class="menu-item">
        <svg class="icon" viewBox="0 0 40 40" fill="none" stroke="var(--text-blue)" stroke-width="1.8">
          <rect x="3" y="14" width="7" height="7"/><rect x="12" y="14" width="7" height="7"/><rect x="21" y="14" width="7" height="7"/>
          <rect x="3" y="23" width="7" height="7"/><rect x="12" y="23" width="7" height="7"/><rect x="21" y="23" width="7" height="7"/>
          <rect x="26" y="5" width="8" height="8" transform="rotate(20 30 9)"/>
        </svg>
        <span class="label">Available Sessions</span>
        <svg class="chevron" viewBox="0 0 20 12"><path d="M2 2 L10 10 L18 2" fill="none" stroke="var(--chevron)" stroke-width="1.6"/></svg>
      </li>
      <li class="menu-item">
        <svg class="icon" viewBox="0 0 40 40" fill="none" stroke="var(--text-blue)" stroke-width="1.8">
          <path d="M8 12 H32 L35 35 H5 Z"/><circle cx="20" cy="7" r="3"/>
          <text x="20" y="28" text-anchor="middle" font-size="9" fill="var(--text-blue)" stroke="none" font-family="Roboto, sans-serif">KG</text>
        </svg>
        <span class="label">Weight Accountability</span>
        <svg class="chevron" viewBox="0 0 20 12"><path d="M2 2 L10 10 L18 2" fill="none" stroke="var(--chevron)" stroke-width="1.6"/></svg>
      </li>
      <li class="menu-item">
        <svg class="icon" viewBox="0 0 40 40" fill="none" stroke="var(--text-blue)" stroke-width="1.8">
          <path d="M4 5 H24 V19 H13 L8 24 V19 H4 Z"/><path d="M16 22 V30 H26 L31 35 V30 H36 V16 H28"/>
        </svg>
        <span class="label">Inbox</span>
        <svg class="chevron" viewBox="0 0 20 12"><path d="M2 2 L10 10 L18 2" fill="none" stroke="var(--chevron)" stroke-width="1.6"/></svg>
      </li>
      <li class="menu-item">
        <svg class="icon" viewBox="0 0 40 40">
          <circle cx="20" cy="20" r="18" fill="var(--text-blue)"/>
          <circle cx="20" cy="15" r="6" fill="#fff"/>
          <path d="M9 32 a11 9 0 0 1 22 0 Z" fill="#fff"/>
        </svg>
        <span class="label">Profile</span>
        <svg class="chevron" viewBox="0 0 20 12"><path d="M2 2 L10 10 L18 2" fill="none" stroke="var(--chevron)" stroke-width="1.6"/></svg>
      </li>
    </ul>
    <div class="list-footer"></div>
  </main>
</body>
</html>
```